New design for Comparison website

We need new design for our website https://kjopsvakten.no/ . We compare prices and providers in different niches such as electricity, mobile plans, broadband etc.

We would like to see design like Pricora com or our competitor valgtopp no

We will need design of all pages, with tables, tables are somewhat different depending on the service compared (use valgtopp no for reference) . Our focus is CTR through comparison Tables.

Final design must communicate following: Professionalism, thrust, authority.

Number of Pages Required

5+ page

Font styles to use
Sans Serif

Colors

Designer to choose colors to be used in the design.

Requirements
Must have
• Tables
Nice to have
• Images in content

```html
<!DOCTYPE html>
<html lang="no">
<head>
<meta charset="utf-8">
<title>Kjopsvakten – compare providers</title>
<link rel="stylesheet" href="https://fonts.googleapis.com/css2?family=Open+Sans:wght@400;600;700&family=Roboto:wght@400;500;700&display=swap">
<style>
:root{
  --green:#12a57e;
  --green-dark:#0d8a69;
  --dark:#3f3f3f;
  --darker:#333;
  --text:#444;
  --muted:#555;
  --light-bg:#f1f1f1;
  --line:#e3e3e3;
  --white:#fff;
}
*{box-sizing:border-box;margin:0;padding:0}
html,body{width:1200px;height:3015px;overflow:hidden}
body{font-family:"Open Sans",sans-serif;color:var(--text);background:var(--white)}
a{color:inherit;text-decoration:none}
.heading{font-family:"Roboto",sans-serif;font-weight:700;color:var(--green);font-size:27px;text-align:center;letter-spacing:.3px}
.heading::after{content:"";display:block;width:92px;height:3px;background:var(--green);margin:18px auto 0}

/* top bar */
.topbar{height:28px;background:var(--dark);color:#eee;font-size:13px;display:flex;align-items:center;justify-content:space-between;padding:0 98px}
.topbar nav{display:flex;gap:0}
.topbar nav a{padding:0 15px;border-left:1px solid #aaa;line-height:12px}
.topbar nav a:first-child{border-left:0}
.topbar nav a:last-child{padding-right:0}

/* header */
.site-header{height:108px;display:flex;align-items:center;justify-content:space-between;padding:0 98px 0 100px}
.brand{display:flex;align-items:center;gap:12px;font-family:"Roboto",sans-serif;font-weight:700;font-size:26px;color:var(--green)}
.brand-mark{width:22px;height:22px;background:var(--green);border-radius:50%}
.main-nav{display:flex;gap:6px;font-family:"Roboto",sans-serif;font-size:16px;color:#222}
.main-nav a{padding:8px 12px;border-radius:2px}
.main-nav a.active{background:var(--green);color:var(--white)}

/* hero */
.hero{position:relative;height:514px;background:linear-gradient(120deg,#5b5650 0%,#7c766e 45%,#4f4b46 100%);color:var(--white);text-align:center}
.hero-title{position:absolute;top:76px;left:0;right:0;font-family:"Roboto",sans-serif;font-size:44px;font-weight:700;letter-spacing:1px}
.hero-sub{position:absolute;top:154px;left:0;right:0;font-size:17px;font-weight:600;line-height:30px}
.hero-arrow{position:absolute;top:232px}
.hero-arrow.prev{left:34px}
.hero-arrow.next{right:34px}

/* about */
.about{height:400px;padding-top:70px;text-align:center}
.about p{width:860px;margin:0 auto;font-size:13px;line-height:25px;color:var(--muted)}
.about .intro{margin-top:30px}
.buttons{margin-top:22px;display:flex;justify-content:center;gap:12px}
.btn{font-family:"Roboto",sans-serif;font-size:15px;font-weight:500;height:44px;padding:0 20px;display:inline-flex;align-items:center;border-radius:3px}
.btn-green{background:var(--green);color:var(--white)}
.btn-outline{border:2px solid #333;color:#222;background:var(--white)}

/* steps */
.steps{height:530px;background:var(--light-bg);padding-top:50px}
.steps-row{position:relative;display:flex;justify-content:space-between;width:1000px;margin:70px auto 0}
.step{width:245px;text-align:center}
.step-icon{position:relative;width:130px;height:130px;margin:0 auto;border-radius:50%;border:3px solid var(--green);display:flex;align-items:center;justify-content:center}
.step-icon .core{width:112px;height:112px;border-radius:50%;background:var(--green);display:flex;align-items:center;justify-content:center}
.step-icon.dark{border-color:#3a3a3a}
.step-icon.dark .core{background:#3a3a3a}
.step-num{position:absolute;top:-10px;right:-6px;width:38px;height:38px;border-radius:50%;background:#3a3a3a;color:var(--white);font-family:"Roboto",sans-serif;font-weight:500;font-size:16px;display:flex;align-items:center;justify-content:center}
.step-num.green{background:var(--green)}
.step h3{margin-top:32px;font-family:"Roboto",sans-serif;font-size:17px;font-weight:700;color:var(--green)}
.step h3.dark{color:#222}
.step h4{margin-top:12px;font-size:14px;font-weight:600;color:#222}
.step p{margin-top:14px;font-size:13px;line-height:22px;color:var(--muted)}
.step-arrow{position:absolute}

/* comparison */
.comparison{height:740px;padding-top:52px}
.plans{display:flex;justify-content:space-between;width:1000px;margin:86px auto 0}
.plan{position:relative;width:318px;height:420px;border:3px solid #222;border-top-width:2px;background:var(--white);text-align:center;box-shadow:0 16px 14px -12px rgba(0,0,0,.25)}
.plan.featured{border-color:var(--green)}
.plan-price{position:absolute;left:50%;top:-68px;transform:translateX(-50%);width:140px;height:140px;border-radius:50%;background:#444;border:5px solid #222;box-shadow:inset 0 0 0 3px #fff;color:var(--white);display:flex;flex-direction:column;align-items:center;justify-content:center;font-family:"Roboto",sans-serif}
.plan.featured .plan-price{background:var(--green);border-color:var(--green)}
.plan-price b{font-size:30px;line-height:34px}
.plan-price span{font-size:19px;font-weight:500}
.plan h3{margin-top:100px;font-family:"Roboto",sans-serif;font-weight:400;font-size:21px;color:#222}
.plan.featured h3{color:var(--green)}
.plan ul{list-style:none;margin-top:16px;border-top:1px solid var(--line)}
.plan li{height:37px;line-height:37px;font-size:13px;color:var(--muted);border-bottom:1px solid var(--line)}
.plan .btn{margin-top:16px;height:40px;padding:0 22px;background:#3a3a3a;color:var(--white);font-size:15px}
.plan.featured .btn{background:var(--green)}

/* cta band */
.cta{display:flex;height:250px}
.cta-half{width:600px;padding:40px 0 0 98px;color:var(--white)}
.cta-green{background:var(--green)}
.cta-dark{background:#474747;padding-left:60px}
.cta h2{font-family:"Roboto",sans-serif;font-weight:500;font-size:23px}
.cta p{margin-top:16px;font-size:13px;font-weight:600;line-height:25px;width:450px}
.btn-ghost{margin-top:22px;border:2px solid var(--white);color:var(--white);height:46px;padding:0 28px;border-radius:0}
.search{margin-top:30px;display:flex;width:440px;height:48px;border:2px solid var(--white)}
.search span{flex:1;display:flex;align-items:center;padding-left:12px;font-size:15px;font-weight:600}
.search i{width:48px;background:var(--green);display:flex;align-items:center;justify-content:center}

/* footer */
.site-footer{height:675px;padding:50px 98px 0}
.footer-cols{display:flex}
.footer-col h4{font-family:"Roboto",sans-serif;font-weight:700;font-size:19px;color:var(--green)}
.footer-col h4::after{content:"";display:block;width:60px;height:2px;background:var(--green);margin-top:14px}
.footer-col ul{list-style:none;margin-top:22px}
.footer-col li{display:flex;align-items:center;gap:10px;font-size:14px;line-height:31px;color:var(--muted)}
.col-pages{width:256px}
.col-services{width:308px}
.col-contact{width:440px}
.form{margin-top:22px;display:grid;grid-template-columns:1fr 1fr;gap:10px 12px}
.field{height:34px;border:1px solid #bbb;border-radius:3px;font-size:11px;padding:7px 8px;color:#333}
.field.wide{grid-column:1/3}
.field.tall{height:64px}
.send{margin-top:12px;display:inline-block;background:var(--green);color:var(--white);font-size:12px;padding:10px 16px;border-radius:2px}
.footer-bottom{margin-top:66px;border-top:1px solid #ccc;padding-top:28px;text-align:center;font-size:13px;font-weight:600;color:#222}
</style>
</head>
<body>

<div class="topbar">
  <span>Welcome To kjopsvakten!</span>
  <nav><a href="#">Home</a><a href="#">About us</a><a href="#">Contact</a><a href="#">Terms</a><a href="#">Privacy</a><a href="#">Cookies</a></nav>
</div>

<header class="site-header">
  <a class="brand" href="https://kjopsvakten.no/"><span class="brand-mark"></span>Kjopsvakten</a>
  <nav class="main-nav">
    <a class="active" href="#">Home</a><a href="#">Broadband</a><a href="#">MMS</a><a href="#">Current</a><a href="#">Hosting and Domains</a><a href="#">Residential Alarm</a>
  </nav>
</header>

<section class="hero" role="img" aria-label="Desk with laptop, tablet, phone, glasses and plant seen from above">
  <h1 class="hero-title">KJOPSVAKTEN</h1>
  <p class="hero-sub">We compare prices and providers in different niches such as electricity, mobile plans,<br>broadband etc...</p>
  <svg class="hero-arrow prev" width="28" height="50" viewBox="0 0 28 50"><path d="M24 3 4 25l20 22" fill="none" stroke="#fff" stroke-width="2"/></svg>
  <svg class="hero-arrow next" width="28" height="50" viewBox="0 0 28 50"><path d="M4 3l20 22L4 47" fill="none" stroke="#fff" stroke-width="2"/></svg>
</section>

<section class="about">
  <h2 class="heading">ABOUT KJOPSVAKTEN</h2>
  <p class="intro">Kjopsvakten.no aims to help consumers find the best providers of services to the best prices. We examine the market and brings together the best in our lists, so you as a consumer can find great deals from reputable players quickly, easily and safely. Nemo enim ipsam voluptatem quia voluptas sit aspernatur aut odit aut fugit, sed quia consequuntur magni dolores.</p>
  <p>Nemo enim ipsam voluptatem quia voluptas sit aspernatur aut odit aut fugit, sed quia consequuntur magni dolores eos qui ratione voluptatem sequi nesciunt.</p>
  <div class="buttons"><a class="btn btn-green" href="#">Read More</a><a class="btn btn-outline" href="#">Contact Us</a></div>
</section>

<section class="steps">
  <h2 class="heading">HOW IT WORKS</h2>
  <div class="steps-row">
    <svg class="step-arrow" style="left:278px;top:20px" width="72" height="30" viewBox="0 0 72 30"><path d="M4 14C24 0 48 2 66 24" fill="none" stroke="#333" stroke-width="2.5"/><path d="M56 22l11 4 0-12" fill="none" stroke="#333" stroke-width="2.5"/></svg>
    <svg class="step-arrow" style="left:640px;top:70px" width="72" height="30" viewBox="0 0 72 30"><path d="M4 16C24 30 48 28 66 6" fill="none" stroke="#333" stroke-width="2.5"/><path d="M54 5l13-1-2 12" fill="none" stroke="#333" stroke-width="2.5"/></svg>
    <div class="step">
      <div class="step-icon"><div class="core"><svg width="46" height="46" viewBox="0 0 46 46"><rect x="5" y="9" width="30" height="30" rx="3" fill="none" stroke="#fff" stroke-width="4"/><path d="M12 22l8 8 20-22" fill="none" stroke="#fff" stroke-width="5"/></svg></div><span class="step-num">1</span></div>
      <h3>SELECT CATEGORY</h3><h4>Read more about the service</h4>
      <p>We collect the most relevant information about the service in one place so that you learn the most important thing in a short time.</p>
    </div>
    <div class="step">
      <div class="step-icon dark"><div class="core"><svg width="46" height="46" viewBox="0 0 46 46"><path d="M8 4h20l8 8v30H8z" fill="none" stroke="#fff" stroke-width="3"/><path d="M13 16h16M13 22h16M13 28h10" stroke="#fff" stroke-width="3"/><path d="M30 38l10-16 3 2-10 16-4 1z" fill="#fff"/></svg></div><span class="step-num green">2</span></div>
      <h3 class="dark">COMPARE PROVIDERS</h3><h4>Choose among the best and most reliable</h4>
      <p>The best and most reputable players compared so you can choose the one that suits you best.</p>
    </div>
    <div class="step">
      <div class="step-icon"><div class="core"><svg width="50" height="40" viewBox="0 0 50 40"><rect x="2" y="6" width="28" height="24" rx="2" fill="#fff"/><path d="M32 12h9l7 9v9H32z" fill="#fff"/><circle cx="12" cy="32" r="5" fill="#fff" stroke="#12a57e" stroke-width="2"/><circle cx="39" cy="32" r="5" fill="#fff" stroke="#12a57e" stroke-width="2"/><path d="M9 18l5 5 9-10" fill="none" stroke="#12a57e" stroke-width="3"/></svg></div><span class="step-num">3</span></div>
      <h3>ORDER SERVICE</h3><h4>Order the best supplier</h4>
      <p>Order the service and enjoy that you've got the best provider quickly and easily.</p>
    </div>
  </div>
</section>

<section class="comparison">
  <h2 class="heading">OUR COMPARISON TABLE</h2>
  <div class="plans">
    <div class="plan featured">
      <div class="plan-price"><b>$0</b><span>free</span></div>
      <h3>Voltra Mobile Plan</h3>
      <ul><li>Nemo enim ipsam voluptatem quia</li><li>Aspernatur aut odit aut fugit, sed quia</li><li>quuntur magni dolores eos ratione</li><li>voluptatem sequi nesciunt neque</li><li>quam est, qui dolorem</li></ul>
      <a class="btn" href="#">Join Now</a>
    </div>
    <div class="plan">
      <div class="plan-price"><b>$45</b><span>month</span></div>
      <h3>Linkel Mobile Plan</h3>
      <ul><li>Nemo enim ipsam voluptatem quia</li><li>Aspernatur aut odit aut fugit, sed quia</li><li>quuntur magni dolores eos ratione</li><li>voluptatem sequi nesciunt neque</li><li>quam est, qui dolorem</li></ul>
      <a class="btn" href="#">Join Now</a>
    </div>
    <div class="plan">
      <div class="plan-price"><b>$60</b><span>month</span></div>
      <h3>Nordiq Mobile Plan</h3>
      <ul><li>Nemo enim ipsam voluptatem quia</li><li>Aspernatur aut odit aut fugit, sed quia</li><li>quuntur magni dolores eos ratione</li><li>voluptatem sequi nesciunt neque</li><li>quam est, qui dolorem</li></ul>
      <a class="btn" href="#">Join Now</a>
    </div>
  </div>
</section>

<section class="cta">
  <div class="cta-half cta-green">
    <h2>Look through the available categories</h2>
    <p>Begin to investigate and compare the providers of the services you need.</p>
    <a class="btn btn-ghost" href="#">START</a>
  </div>
  <div class="cta-half cta-dark">
    <h2>Those who seek shall find</h2>
    <p>See if you use the best provider of services.</p>
    <div class="search"><span>Search</span><i><svg width="16" height="16" viewBox="0 0 16 16"><circle cx="6.5" cy="6.5" r="4.5" fill="none" stroke="#fff" stroke-width="2"/><path d="M10 10l4.5 4.5" stroke="#fff" stroke-width="2"/></svg></i></div>
  </div>
</section>

<footer class="site-footer">
  <div class="footer-cols">
    <div class="footer-col col-pages">
      <h4>RELATED PAGES</h4>
      <ul>
        <li><svg width="12" height="10" viewBox="0 0 12 10"><path d="M1 5h9M6 1l4 4-4 4" fill="none" stroke="#12a57e" stroke-width="1.8"/></svg>Home</li>
        <li><svg width="12" height="10" viewBox="0 0 12 10"><path d="M1 5h9M6 1l4 4-4 4" fill="none" stroke="#12a57e" stroke-width="1.8"/></svg>About Us</li>
        <li><svg width="12" height="10" viewBox="0 0 12 10"><path d="M1 5h9M6 1l4 4-4 4" fill="none" stroke="#12a57e" stroke-width="1.8"/></svg>Contact</li>
        <li><svg width="12" height="10" viewBox="0 0 12 10"><path d="M1 5h9M6 1l4 4-4 4" fill="none" stroke="#12a57e" stroke-width="1.8"/></svg>Terms</li>
        <li><svg width="12" height="10" viewBox="0 0 12 10"><path d="M1 5h9M6 1l4 4-4 4" fill="none" stroke="#12a57e" stroke-width="1.8"/></svg>Privacy</li>
        <li><svg width="12" height="10" viewBox="0 0 12 10"><path d="M1 5h9M6 1l4 4-4 4" fill="none" stroke="#12a57e" stroke-width="1.8"/></svg>Cookies</li>
      </ul>
    </div>
    <div class="footer-col col-services">
      <h4>COMPARE SERVICES</h4>
      <ul>
        <li><svg width="12" height="10" viewBox="0 0 12 10"><path d="M1 5h9M6 1l4 4-4 4" fill="none" stroke="#12a57e" stroke-width="1.8"/></svg>Cheap MMS</li>
        <li><svg width="12" height="10" viewBox="0 0 12 10"><path d="M1 5h9M6 1l4 4-4 4" fill="none" stroke="#12a57e" stroke-width="1.8"/></svg>Current</li>
        <li><svg width="12" height="10" viewBox="0 0 12 10"><path d="M1 5h9M6 1l4 4-4 4" fill="none" stroke="#12a57e" stroke-width="1.8"/></svg>Web Hosting</li>
        <li><svg width="12" height="10" viewBox="0 0 12 10"><path d="M1 5h9M6 1l4 4-4 4" fill="none" stroke="#12a57e" stroke-width="1.8"/></svg>Residential Alarm</li>
        <li><svg width="12" height="10" viewBox="0 0 12 10"><path d="M1 5h9M6 1l4 4-4 4" fill="none" stroke="#12a57e" stroke-width="1.8"/></svg>Broadband</li>
        <li><svg width="12" height="10" viewBox="0 0 12 10"><path d="M1 5h9M6 1l4 4-4 4" fill="none" stroke="#12a57e" stroke-width="1.8"/></svg>To Me</li>
      </ul>
    </div>
    <div class="footer-col col-contact">
      <h4>CONTACT US</h4>
      <div class="form">
        <div class="field">Name</div><div class="field">Email</div>
        <div class="field wide">Subject</div>
        <div class="field wide tall">Message</div>
      </div>
      <a class="send" href="#">SEND MESSAGE</a>
    </div>
  </div>
  <div class="footer-bottom">Copyrights @ 2017 Kjopsvakten. All rights reserved.</div>
</footer>

</body>
</html>
```